Thornbury Group needs a business card

I would like the card to be simple but modern and elegant.
I like black and white.
or black and gold.
we are a private finance lender and also are involved in property and property developments.

please look at the business card photos i provided i would like T.G only one one side and all the other details on the other side use fonts that tie in with my theme.

Industry/Entity Type

Finance

Contact Information for Business Card

Thornbury Group (T.G) Marcus Thornbury M: 0418593062 E: marcusthorn@quillmail.example

Font styles to use
Other font styles liked:
• Use fonts that would reflect our business

Colors
000000
ffffff

Requirements
Must have
• one side of details
• other side has either T.G or Thornbury Group like in the photos provided

```html
<!DOCTYPE html>
<html lang="en">
<head>
<meta charset="utf-8">
<title>Thornbury Group — Business Card</title>
<link rel="stylesheet" href="https://fonts.googleapis.com/css2?family=Montserrat:wght@300;400;700&display=swap">
<style>
  :root {
    --backdrop: #2b2b2d;
    --card-black: #121212;
    --gold: #e2c47c;
    --gold-soft: #cdb06a;
  }
  * { margin: 0; padding: 0; box-sizing: border-box; }
  html, body {
    width: 1200px;
    height: 786px;
    overflow: hidden;
    background: var(--backdrop);
  }
  .canvas {
    position: relative;
    width: 1200px;
    height: 786px;
    display: flex;
    align-items: center;
    justify-content: center;
    gap: 60px;
    font-family: "Montserrat", Arial, sans-serif;
  }
  .card {
    width: 500px;
    height: 305px;
    background: var(--card-black);
    box-shadow: 0 18px 40px rgba(0, 0, 0, 0.45);
    display: flex;
    flex-direction: column;
    align-items: center;
    justify-content: center;
    color: var(--gold);
  }
  .card--details { padding-top: 6px; }
  .holder-name {
    font-weight: 700;
    font-size: 22px;
    letter-spacing: 1.5px;
    text-transform: uppercase;
  }
  .contact-line {
    margin-top: 16px;
    font-weight: 300;
    font-size: 14px;
    letter-spacing: 0.8px;
    color: var(--gold-soft);
  }
  .contact-line .divider { margin: 0 6px; }
  .company-name {
    margin-top: 18px;
    font-weight: 700;
    font-size: 10px;
    letter-spacing: 1.2px;
    text-transform: uppercase;
  }
  .brand-name {
    font-weight: 400;
    font-size: 30px;
    letter-spacing: 3px;
    line-height: 1;
    text-transform: uppercase;
    color: var(--gold);
  }
</style>
</head>
<body>
  <main class="canvas">
    <section class="card card--details">
      <h1 class="holder-name">Marcus Thornbury</h1>
      <p class="contact-line">M. 0418593062<span class="divider">|</span>E. marcusthorn@quillmail.example</p>
      <p class="company-name">Thornbury Group</p>
    </section>
    <section class="card card--brand">
      <p class="brand-name">Thornbury Group</p>
    </section>
  </main>
</body>
</html>
```